Thornwell Building Company - advertisement poster

I am looking to print some canvas signs to advertise my general contracting company, Thornwell Building Company. The sign will measure 6' long x 3' high so the size should match that ratio. I already have a logo icon, which is the Letter 'A' and some trees that I would like to incorporate, see attached. I would also like the to have the following information listed:
1) phone number: 472-318-6095
2) email: thornwellbuildingcompany@mailvistra.net
3) website: thornwellbuildingcompany.com
4) Lic#5386204
5) I want to use this text: "BUILD WITH THE T-CREW!"

The ad should be relatively simple and clean. Black and Green are my company colors. I am open to creative ideas!

Target Market(s)

People looking to renovate their homes

Industry/Entity Type

Construction

Colors
59FF00
82FF00
B8FF75
E3FFCB
F4FFEA

Requirements
Must have
• Must have my company logo
Should not have
• No photos or complex graphics

```html
<!DOCTYPE html>
<html lang="en">
<head>
<meta charset="utf-8">
<title>Thornwell Building Company – Sign</title>
<link rel="stylesheet" href="https://fonts.googleapis.com/css2?family=Audiowide&family=Orbitron:wght@700;800&display=swap">
<style>
  :root {
    --backdrop: #b5b5b5;
    --green: #6ab330;
    --green-deep: #4f8f22;
    --navy: #171b62;
    --white: #ffffff;
  }
  html, body {
    margin: 0;
    width: 1200px;
    height: 1200px;
    overflow: hidden;
    background: var(--backdrop);
  }
  .canvas {
    position: relative;
    width: 1200px;
    height: 1200px;
    display: flex;
    align-items: center;
    justify-content: center;
  }
  .sign {
    width: 1040px;
    height: 520px;
    display: block;
  }
  .headline { font-family: "Orbitron", sans-serif; font-weight: 800; fill: var(--white); }
  .headline-sub { letter-spacing: 9px; }
  .license { font-family: "Audiowide", sans-serif; font-size: 11px; letter-spacing: 6px; fill: var(--white); text-anchor: middle; }
  .company-name { font-family: "Orbitron", sans-serif; font-weight: 700; fill: var(--white); text-anchor: middle; }
  .established { font-family: "Audiowide", sans-serif; font-size: 12px; letter-spacing: 4px; fill: var(--white); text-anchor: middle; }
  .contact { font-family: "Audiowide", sans-serif; text-anchor: middle; }
  .contact-phone { fill: var(--navy); letter-spacing: 6px; }
  .contact-divider { fill: var(--navy); }
  .contact-web { fill: var(--green); }
  .contact-mail { fill: var(--navy); }
</style>
</head>
<body>
<main class="canvas">
  <svg class="sign" viewBox="0 0 1040 520" xmlns="http://www.w3.org/2000/svg" role="img" aria-label="Thornwell Building Company sign: Build with the T-Crew">
    <defs>
      <linearGradient id="contact-band-fade" x1="0" y1="0" x2="0" y2="1">
        <stop offset="0.7" stop-color="#ffffff"/>
        <stop offset="1" stop-color="#e6e6e6"/>
      </linearGradient>
    </defs>

    <rect class="contact-band" x="0" y="0" width="1040" height="520" fill="url(#contact-band-fade)"/>

    <rect class="brand-panel" x="0" y="0" width="1040" height="392" fill="var(--navy)"/>

    <polygon class="headline-panel" fill="var(--green)"
      points="0,0 655,0 515,183 559,186 486,282 535,284 459,386 0,386"/>

    <polygon fill="var(--navy)" points="0,0 58,0 42,12 34,10 0,55"/>

    <polygon fill="var(--white)" points="885,0 1040,0 1040,144 963,53 949,65"/>

    <polyline fill="none" stroke="var(--green-deep)" stroke-width="1.5"
      points="0,370 450,370 480,338 520,338"/>

    <text class="headline" x="36" y="118" font-size="76">BUILD</text>
    <text class="headline headline-sub" x="38" y="188" font-size="54">WITH THE</text>
    <text class="headline" x="36" y="262" font-size="72">T-CREW!</text>

    <rect class="ornament-area" x="36" y="280" width="420" height="40" fill="var(--green-deep)"
      role="img" aria-label="Decorative wavy line with a row of dots"/>

    <text class="license" x="246" y="348">Lic#5386204</text>

    <rect class="brand-mark" x="742" y="78" width="100" height="100" fill="var(--green)"/>
    <text class="company-name" x="792" y="262" font-size="40">THORNWELL</text>
    <text class="company-name" x="792" y="296" font-size="17" letter-spacing="5">BUILDING COMPANY</text>

    <line x1="726" y1="350" x2="770" y2="350" stroke="var(--green)" stroke-width="1.5"/>
    <line x1="812" y1="350" x2="862" y2="350" stroke="var(--green)" stroke-width="1.5"/>
    <line x1="791" y1="328" x2="791" y2="352" stroke="var(--green)" stroke-width="1.5"/>
    <text class="established" x="749" y="344">ESTD</text>
    <text class="established" x="837" y="344">2020</text>

    <text class="contact contact-row" x="520" y="446">
      <tspan class="contact-phone" font-size="26">472-318-6095</tspan>
      <tspan class="contact-divider" font-size="26" dx="12">|</tspan>
      <tspan class="contact-web" font-size="23" dx="12">thornwellbuildingcompany.com</tspan>
    </text>
    <text class="contact contact-mail" x="520" y="488" font-size="25">thornwellbuildingcompany@mailvistra.net</text>
  </svg>
</main>
</body>
</html>
```